Spooky Sweets Night

I am an intern at Marlow Ridge Community College, and Campus Council is hosting a Spooky Sweets Night in the Johnson County area. I am looking for a digital flyer to use for the event. Here are details for this year's event and info from last year. If you have any questions, please let me know. Last year's flyer is attached below.

Date: Friday, Oct. 25th, 2019
Location: Pellham Hall (Ground Floor)
Theme: Cats & Bats
Exciting Activities Include:
-(Glowing) Footsteps showing the path the kids should go?
-Face painting
-Cotton Candy
-Fog Machine w/bubbles
-Candy sponsorship (Fresko or Oak Basket)
-Encouraging the community to bring food donations for MRCC Food Pantry

```html
<!DOCTYPE html>
<html lang="en">
<head>
<meta charset="utf-8">
<title>Spooky Sweets Night</title>
<link rel="stylesheet" href="https://fonts.googleapis.com/css2?family=Chewy&family=Mystery+Quest&family=Arimo:wght@400;700&display=swap">
<style>
  :root {
    --night-purple: #4a2e6b;
    --deep-purple: #2e1a47;
    --glow-purple: #6a4a8f;
    --candy-yellow: #f7d21e;
    --pumpkin-orange: #f5a31c;
    --title-pink: #b2479b;
    --soft-lilac: #e9dcf5;
    --white: #ffffff;
    --bat-black: #1b1320;
    --balloon-orange: #f08a1e;
  }
  * { margin: 0; padding: 0; box-sizing: border-box; }
  html, body { width: 984px; height: 1200px; overflow: hidden; background: var(--deep-purple); }
  .flyer {
    position: relative;
    width: 984px;
    height: 1200px;
    overflow: hidden;
    background: radial-gradient(ellipse at 60% 45%, var(--glow-purple) 0%, var(--night-purple) 45%, var(--deep-purple) 100%);
    font-family: "Arimo", Arial, sans-serif;
  }
  .art { position: absolute; }
  .art--balloons-cat {
    left: 50px; top: 70px; width: 350px; height: 1110px;
    border-radius: 175px 175px 160px 160px;
    background: linear-gradient(180deg, #e8e4e0 0%, var(--pumpkin-orange) 22%, var(--balloon-orange) 45%, #3a2a4a 60%, var(--balloon-orange) 85%, #f3b23a 100%);
    opacity: 0.85;
  }
  .art--web {
    left: 300px; top: 8px; width: 200px; height: 155px;
    border-radius: 0 0 100px 100px;
    background: radial-gradient(ellipse at 50% 0%, rgba(255,255,255,0.28), rgba(255,255,255,0.04) 70%);
  }
  .art--bunting {
    left: 526px; top: 0; width: 430px; height: 210px;
    background: linear-gradient(165deg, transparent 0 30%, var(--balloon-orange) 30% 45%, #7a3fa0 45% 60%, var(--bat-black) 60% 75%, transparent 75%);
    opacity: 0.9;
  }
  .art--bat-large {
    left: 380px; top: 532px; width: 245px; height: 175px;
    border-radius: 50% 50% 40% 40%;
    background: radial-gradient(ellipse at 50% 50%, #2a1f30 0%, var(--bat-black) 60%, transparent 72%);
  }
  .art--bat-small {
    left: 772px; top: 772px; width: 115px; height: 62px;
    border-radius: 50%;
    background: radial-gradient(ellipse at 50% 50%, var(--bat-black) 0%, var(--bat-black) 45%, transparent 70%);
  }
  .title {
    position: absolute; left: 450px; top: 70px; width: 480px;
    text-align: center;
    font-family: "Chewy", cursive;
    line-height: 1;
  }
  .title__top {
    display: block; font-size: 112px; color: var(--title-pink);
    text-shadow: 0 4px 0 var(--candy-yellow);
  }
  .title__main {
    display: block; margin-top: 70px; font-size: 150px; color: var(--candy-yellow);
    text-shadow: 0 5px 0 var(--balloon-orange);
  }
  .title__sub {
    display: block; margin-top: 4px; font-size: 58px; color: var(--soft-lilac);
  }
  .date {
    position: absolute; left: 512px; top: 545px; width: 320px;
    text-align: center; color: var(--candy-yellow);
  }
  .date__day { display: block; font-family: "Mystery Quest", cursive; font-size: 76px; line-height: 1; }
  .date__month, .date__weekday { display: block; font-size: 36px; line-height: 1.05; letter-spacing: 1px; }
  .venue {
    position: absolute; left: 430px; top: 730px; width: 484px;
    text-align: center; color: var(--white); font-size: 28px;
  }
  .theme {
    position: absolute; left: 432px; top: 790px; width: 480px;
    text-align: center; font-family: "Mystery Quest", cursive;
    color: var(--pumpkin-orange); line-height: 1.15;
  }
  .theme__label { display: block; font-size: 50px; }
  .theme__name { display: block; font-size: 56px; }
  .activities {
    position: absolute; left: 407px; top: 918px; width: 560px;
    color: var(--white); font-size: 17px;
  }
  .activities__heading {
    text-align: center; color: var(--candy-yellow); font-size: 17px;
    font-weight: 400; margin-bottom: 10px; padding-right: 60px;
  }
  .activities__list { list-style: none; line-height: 29.5px; }
  .activities__list li::before { content: "\2022\00a0"; }
  .activities__list .continued::before { content: ""; }
</style>
</head>
<body>
  <main class="flyer">
    <div class="art art--balloons-cat" role="img" aria-label="Halloween balloons with jack-o'-lantern and skull designs above a black cat in a witch hat sitting in a pumpkin"></div>
    <div class="art art--web" role="img" aria-label="Spider web with a small spider hanging from a thread"></div>
    <div class="art art--bunting" role="img" aria-label="Orange, purple and black party bunting"></div>
    <div class="art art--bat-large" role="img" aria-label="Cartoon bat flying"></div>
    <div class="art art--bat-small" role="img" aria-label="Small cartoon bat"></div>

    <h1 class="title">
      <span class="title__top">Spooky</span>
      <span class="title__main">Sweets</span>
      <span class="title__sub">Night</span>
    </h1>

    <p class="date">
      <span class="date__day">25</span>
      <span class="date__month">OCTOBER</span>
      <span class="date__weekday">FRIDAY</span>
    </p>

    <p class="venue">Pellham Hall (Ground Floor)</p>

    <p class="theme">
      <span class="theme__label">THEME:</span>
      <span class="theme__name">CATS &amp; BATS</span>
    </p>

    <section class="activities">
      <h2 class="activities__heading">EXCITING ACTIVITIES INCLUDE:</h2>
      <ul class="activities__list">
        <li>(Glowing) Footsteps showing the path the kids should go?</li>
        <li>Face painting</li>
        <li>Cotton Candy</li>
        <li>Fog Machine w/bubbles</li>
        <li>Candy sponsorship (Fresko or Oak Basket)</li>
        <li>Encouraging the community to bring</li>
        <li class="continued">food donations for MRCC Food Pantry</li>
      </ul>
    </section>
  </main>
</body>
</html>
```